political campaign lawn sign - Governor's Council in Massachuesetts

We are looking for a political lawn sign. We are running a campaign for Governor's Council in Massachusetts. This sign will be on the lawn of homes and businesses so people driving by will see it. It needs to be simple and bold. The last name is long so maybe it could say vote for Marty and then Kolbeck will be big a bold on the next line??
We need it to say:
Vote for Martin Kolbeck
Governor's Council.

Target Market(s)

local residents

Industry/Entity Type

Politcal Campaign

Font styles to use
Sans Serif
Other font styles liked:
• not sure what font but a modern looking one such as Helvetica, Arial, Sans Seri, sharp sans..

Colors
0054AA
0677BA
7BADD7
CADEEF
E8F1F8
00AB8E
00BBA5
67D7C9
C6EFE9
E9F9F6
FFF300
FFF600
FEFA6F
FFFEC7
FFFEE8

Requirements
Must have
• My name written out with a Capital D and R but lower case for every other letter so its Marty Kolbeck
Nice to have
• modern font , the Colors of the lawn sign should have Blue, Yellow and White something bold that will stand out
Should not have
• any maps of Massachusetts

```html
<!DOCTYPE html>
<html lang="en">
<head>
<meta charset="utf-8">
<title>Marty Kolbeck – Governor's Council Lawn Sign</title>
<link rel="stylesheet" href="https://fonts.googleapis.com/css2?family=Anton&family=Montserrat:wght@600;700;800&family=Oswald:wght@700&display=swap">
<style>
  :root {
    --page-bg: #e6e6e6;
    --sign-blue: #0054aa;
    --navy: #0a1f6e;
    --name-top: #0b1d6b;
    --name-bottom: #0054aa;
    --sign-yellow: #fff300;
    --white: #ffffff;
  }
  html, body {
    margin: 0;
    padding: 0;
    width: 888px;
    height: 1200px;
    overflow: hidden;
    background: var(--page-bg);
  }
  .canvas {
    position: relative;
    width: 888px;
    height: 1200px;
  }
  .lawn-sign {
    position: absolute;
    left: 44px;
    top: 315px;
    width: 800px;
    height: 571px;
    display: block;
  }
  .sign-frame { fill: var(--sign-blue); }
  .sign-panel { fill: var(--white); }
  .accent-band { fill: var(--sign-yellow); }
  .ribbon-text {
    font-family: "Oswald", "Anton", sans-serif;
    font-weight: 700;
    fill: var(--navy);
  }
  .candidate-name {
    font-family: "Anton", "Oswald", sans-serif;
  }
  .office-title {
    font-family: "Montserrat", sans-serif;
    font-weight: 800;
    fill: var(--navy);
  }
  .web-address {
    font-family: "Montserrat", sans-serif;
    font-weight: 700;
    fill: var(--white);
  }
  .web-highlight { fill: var(--sign-yellow); }
</style>
</head>
<body>
<main class="canvas">
  <svg class="lawn-sign" viewBox="0 0 800 571" xmlns="http://www.w3.org/2000/svg" aria-label="Vote for Marty Kolbeck, Governor's Council lawn sign">
    <defs>
      <linearGradient id="first-name-fill" gradientUnits="userSpaceOnUse" x1="0" y1="55" x2="0" y2="167">
        <stop offset="0" stop-color="var(--name-top)"/>
        <stop offset="1" stop-color="var(--name-bottom)"/>
      </linearGradient>
      <linearGradient id="last-name-fill" gradientUnits="userSpaceOnUse" x1="0" y1="177" x2="0" y2="338">
        <stop offset="0" stop-color="var(--name-top)"/>
        <stop offset="1" stop-color="var(--name-bottom)"/>
      </linearGradient>
      <clipPath id="sign-clip">
        <rect x="0" y="0" width="800" height="571"/>
      </clipPath>
    </defs>

    <rect class="sign-frame" x="0" y="0" width="800" height="571"/>
    <path class="sign-panel" d="M19 375 V31 Q19 17 33 17 H767 Q781 17 781 31 V375 Z"/>

    <g class="vote-ribbon" clip-path="url(#sign-clip)">
      <polygon class="accent-band" points="162,0 269,0 0,209 0,128"/>
      <text class="ribbon-text" x="0" y="0" font-size="40" text-anchor="middle"
            transform="translate(108 108) rotate(-38)">VOTE FOR</text>
    </g>

    <text class="candidate-name" x="440" y="167" font-size="130" text-anchor="middle"
          fill="url(#first-name-fill)" textLength="330" lengthAdjust="spacingAndGlyphs">Marty</text>
    <text class="candidate-name" x="398" y="338" font-size="187" text-anchor="middle"
          fill="url(#last-name-fill)" textLength="650" lengthAdjust="spacingAndGlyphs">Kolbeck</text>

    <rect class="accent-band" x="19" y="375" width="762" height="66"/>
    <text class="office-title" x="400" y="423" font-size="44" text-anchor="middle"
          textLength="606" lengthAdjust="spacingAndGlyphs">GOVERNOR'S COUNCIL</text>

    <text class="web-address" x="400" y="532" font-size="92" text-anchor="middle"
          textLength="706" lengthAdjust="spacingAndGlyphs">votefor<tspan class="web-highlight">marty</tspan>.net</text>
  </svg>
</main>
</body>
</html>
```